Nicht nur, dass ich mit dem Design sehr zufrieden war, auch Änderungswünsche wurden zeitnah und zu meiner vollen Zufriedenheit ausgeführt.
Zielgruppe
Ich schreibe Kriminalromane
Zielgruppe sind die Leser von Kriminalromanen, Regionalkrimis
Aufgabenstellung
Hier handelt es sich um eine Kindesentführung im ländlichen Raum (Bayerischer Wald) ein Mosaik von Inzest und Tod.
Der Titel in moderner Schrift, angelehnt an die Titel der Skandinavienkrimis, sollte auch in kleiner Abbildung gut lesbar sein.
Es kommen in Kürze zwei weitere Titel, ebenfalls Kriminalromane, das Cover sollte also so gestaltet sein, dass eine durchgängige Reihe möglich ist.

```html
<!DOCTYPE html>
<html lang="de">
<head>
<meta charset="utf-8">
<title>Die Akte Wendel – Buchcover</title>
<link href="https://fonts.googleapis.com/css2?family=Arimo:wght@400;700&display=swap" rel="stylesheet">
<style>
  :root {
    --page-bg: #ececec;
    --cover-red: #c8161b;
    --label-red: #d2232a;
    --label-text: #ffffff;
    --sky-top: #3f6f8a;
    --sky-mid: #9fb9c6;
    --village-light: #cbb89c;
    --village-dark: #6e5f4f;
  }
  html, body {
    margin: 0;
    padding: 0;
    width: 1200px;
    height: 960px;
    overflow: hidden;
    background: var(--page-bg);
    font-family: "Arimo", Arial, sans-serif;
  }
  .book-cover {
    position: absolute;
    left: 280px;
    top: 57px;
    width: 640px;
    height: 846px;
    background: var(--cover-red);
  }
  .cover-photo {
    position: absolute;
    left: 63px;
    top: 61px;
    width: 514px;
    height: 728px;
    background: linear-gradient(180deg,
      var(--sky-top) 0%,
      var(--sky-mid) 30%,
      #d9dcd6 52%,
      var(--village-light) 65%,
      #a89478 82%,
      var(--village-dark) 100%);
  }
  .title-block {
    position: absolute;
    left: 40px;
    top: 58px;
  }
  .title-line {
    display: table;
    background: var(--label-red);
    color: var(--label-text);
    font-weight: 700;
    font-size: 70px;
    line-height: 78px;
    padding: 0 12px 0 10px;
    margin-bottom: 4px;
    letter-spacing: 0.5px;
  }
  .title-meta {
    display: table;
    margin-top: 9px;
    background: var(--label-red);
    color: var(--label-text);
    font-size: 13px;
    line-height: 24px;
    padding: 0 9px 0 7px;
  }
</style>
</head>
<body>
  <div class="book-cover">
    <div class="cover-photo" role="img" aria-label="Foto: Blick durch ein zerrissenes Fliegengitter auf eine Dorfstraße mit Häusern, Straßenlaterne und bewölktem Himmel">
      <div class="title-block">
        <h1 style="margin:0;font:inherit;">
          <span class="title-line">DIE AKTE</span>
          <span class="title-line">WENDEL</span>
        </h1>
        <p class="title-meta" style="margin-bottom:0;">Kriminalroman | Jonas Eberhardt</p>
      </div>
    </div>
  </div>
</body>
</html>
```